Ich bin eine Beraterin mit sehr unterschiedlichen Zugängen. Zum einen mache ich hellsichtige Beratungen, zum anderen Organisationsberatungen und Coaching. Ich habe für jedes Problem eine Lösung. Es handelt sich um eine außergewöhnliche Dienstleistung. Es geht um mehr Klarheit und Transparenz. Meine Kunden sind sowohl Privatpersonen, als auch Firmeninhaber und Firmenchefs kleiner und großer Unternehmen.
I am a consultant with different approaches. On one hand I am doing perceptive consulting, on the other hand I do systemic consulting of organizations and coaching. I find a solution for every problem. It is an outstanding service. Clearness and transparency are mainly wished. My clients are private persons as well as company owners and managers of small and huge companies.
Das Logo soll nur den Vor- und Nachnamen beinhalten und elegant, weiblich, warm, herzlich sein sowie Lebensfreude, Erleichterung und Exklusivität suggerieren.
Das Logo soll auf den Visitenkarten auf der Rückseite geprägt werden. Es soll aber auch für Briefpapier, Powerpoint-Vorlage und Website gut tauglich sein.
The logo should include only my full name. It should be elegant, female, warm, sincere as well as suggest joie de vivre, easement and exclusiveness.
The logo should be stamped on the back side of the business cards. It should also work for letters, PowerPoint presentations and on the website.

```html
<!DOCTYPE html>
<html lang="de">
<head>
<meta charset="utf-8">
<title>Ines Walkemper – Geschäftsausstattung</title>
<link href="https://fonts.googleapis.com/css2?family=Roboto+Condensed:wght@300;400;700&display=swap" rel="stylesheet">
<style>
  :root {
    --gold: #b69b62;
    --cream: #ecdfc6;
    --cream-soft: #f6efe2;
    --text-grey: #7a7a7a;
    --paper: #ffffff;
  }
  * { margin: 0; padding: 0; box-sizing: border-box; }
  html, body { width: 1200px; height: 1155px; overflow: hidden; background: var(--paper); }
  body { position: relative; font-family: "Roboto Condensed", Arial, sans-serif; color: var(--text-grey); }

  .letterhead {
    position: absolute; left: 131px; top: 158px; width: 595px; height: 842px;
    background: var(--paper); box-shadow: 0 0 4px rgba(0,0,0,.25); overflow: hidden;
  }
  .wordmark {
    position: absolute; white-space: nowrap; color: var(--gold);
    font-weight: 700; text-transform: uppercase; transform: translateX(-50%);
  }
  .letterhead .wordmark { left: 297px; top: 82px; font-size: 12px; letter-spacing: 5.6px; }
  .sender-line {
    position: absolute; left: 67px; top: 167px; font-size: 7.5px;
    border-bottom: 0.8px solid #b5b5b5; padding: 0 3px 2px;
  }
  .sender-line .dot { display: inline-block; width: 3px; height: 3px; border-radius: 50%; background: var(--gold); margin: 0 9px 1px; vertical-align: middle; }
  .contact-block { position: absolute; left: 438px; top: 166px; font-size: 8.4px; line-height: 12.8px; }
  .contact-block .gap { height: 10px; }
  .bank-block { position: absolute; left: 444px; top: 716px; font-size: 8.4px; line-height: 12px; }
  .bank-block .gap { height: 7px; }

  .footer-band { position: absolute; left: 0; right: 0; bottom: 0; background: var(--gold); }
  .footer-band::before {
    content: ""; position: absolute; left: 0; right: 0; top: -6px; height: 3px; background: var(--cream);
  }
  .letterhead .footer-band { height: 62px; }

  .wordmark.standalone { left: 938px; top: 296px; font-size: 22px; letter-spacing: 11px; }

  .card { position: absolute; box-shadow: 0 0 4px rgba(0,0,0,.25); overflow: hidden; }
  .card-front { left: 670px; top: 476px; width: 320px; height: 206px; background: var(--gold); }
  .card-front .wordmark { left: 160px; top: 107px; font-size: 13px; letter-spacing: 6.5px; color: #fff; }

  .card-back { left: 761px; top: 702px; width: 329px; height: 212px; background: var(--paper); }
  .card-back .footer-band { height: 26px; }
  .keyword-area {
    position: absolute; left: 14px; top: 30px; width: 158px; height: 128px;
    background: radial-gradient(ellipse at 50% 45%, var(--cream) 0%, var(--cream-soft) 55%, var(--paper) 100%);
  }
  .card-divider { position: absolute; left: 184px; top: 45px; width: 1px; height: 133px; background: var(--gold); }
  .card-details { position: absolute; left: 194px; top: 46px; font-size: 9.6px; line-height: 13.6px; color: var(--gold); }
  .card-details .name { font-weight: 700; font-size: 11.2px; }
  .card-details .gap { height: 19px; }
  .card-details .gap-sm { height: 6px; }
  .card-details .gap-xs { height: 3px; }
</style>
</head>
<body>

<section class="letterhead">
  <div class="wordmark">Ines Walkemper</div>
  <div class="sender-line">Ines Walkemper<span class="dot"></span>Musterstraße 00<span class="dot"></span>12345 Musterstadt</div>
  <div class="contact-block">
    <div>Ines Walkemper</div><div>Titel</div><div>Musterstraße 12</div><div>12345 Musterstadt</div>
    <div class="gap"></div>
    <div>T. 0123 456 789</div><div>F. 0123 456 789</div><div>info@ineswalkemper.de</div><div>www.ineswalkemper.de</div>
  </div>
  <div class="bank-block">
    <div>Steuernr.: 123/456/78910</div>
    <div class="gap"></div>
    <div>Bankverbindung:</div><div>IBAN: DE12 3456 789 1253 5708 40</div><div>BIC: &nbsp;&nbsp; MUSTDEF1234</div>
  </div>
  <div class="footer-band"></div>
</section>

<div class="wordmark standalone">Ines Walkemper</div>

<section class="card card-front">
  <div class="wordmark">Ines Walkemper</div>
</section>

<section class="card card-back">
  <div class="keyword-area" role="img" aria-label="Dekorative Wortwolke mit den Leistungen Coaching, Mediation und Organisationsberatung"></div>
  <div class="card-divider"></div>
  <div class="card-details">
    <div class="name">INES WALKEMPER</div>
    <div>Titel</div>
    <div class="gap"></div>
    <div>Musterstraße 12</div><div>12345 Musterstadt</div>
    <div class="gap-sm"></div>
    <div>T. 0123 456 789</div><div>F. 0123 456 789</div>
    <div class="gap-xs"></div>
    <div>info@ineswalkemper.de</div><div>www.ineswalkemper.de</div>
  </div>
  <div class="footer-band"></div>
</section>

</body>
</html>
```